Travesco Business Cards

We need a business card design for Travesco Mining.

This is a B2B company that buys and sells large machinery tires within the coal mining industry. The design should the strong, crisp and masculine. I have uploaded the company logo and rough mock-up of what the back of the card should look like. the front of the card should have the same look/feel as the back. I need editable templates for both the front and the back of the card.

Color scheme should be grey/green/black

Contact information to include on the card:
Name: Dale Pemberton
Title: Managing Director
Phone: 214-503-6192
Address: 1185 Wexley #3 Dallas, TX 75211
Email: Dale@Travesco-example.com

I am also opening a contest for letterhead design. If you submit a business card design, please also submit a letterhead design with the same look/feel. The winner of the business card design will also will the letter head and be paid for both.

Target Market(s)

Procurement men/women in the coal mining industry

Industry/Entity Type

Coal Mining

```html
<!DOCTYPE html>
<html lang="en">
<head>
<meta charset="utf-8">
<title>Travesco Mining Business Card</title>
<link rel="stylesheet" href="https://fonts.googleapis.com/css2?family=Source+Sans+3:wght@400;700&display=swap">
<style>
  :root {
    --bg: #e4e4e2;
    --card-black: #0b0b0b;
    --green: #6ab43e;
    --white: #ffffff;
    --grey-text: #d8d8d8;
  }
  html, body {
    margin: 0;
    padding: 0;
    width: 1200px;
    height: 1024px;
    overflow: hidden;
    background: var(--bg);
    font-family: "Source Sans 3", Arial, sans-serif;
  }
  .canvas {
    position: relative;
    width: 1200px;
    height: 1024px;
  }
  .card {
    position: absolute;
    left: 270px;
    width: 660px;
    height: 377px;
    background: var(--card-black);
    overflow: hidden;
    box-shadow: 0 6px 18px rgba(0,0,0,0.25);
  }
  .card-front { top: 90px; }
  .card-back { top: 557px; }
  .card svg.shapes {
    position: absolute;
    inset: 0;
  }
  .wordmark {
    position: absolute;
    left: 70px;
    top: 78px;
  }
  .wordmark-name {
    font-weight: 700;
    font-size: 50px;
    letter-spacing: 3px;
    color: var(--white);
    line-height: 1;
  }
  .wordmark-sub {
    margin-top: 6px;
    font-weight: 700;
    font-size: 15px;
    letter-spacing: 25px;
    color: var(--green);
  }
  .contact {
    position: absolute;
    left: 70px;
    top: 188px;
    font-size: 17px;
    line-height: 25px;
    color: var(--grey-text);
  }
  .contact .label { color: var(--green); }
  .contact .title { color: var(--green); margin-bottom: 12px; }
  .contact .value { color: var(--white); }
  .back-name {
    position: absolute;
    left: 250px;
    top: 150px;
    font-weight: 700;
    font-size: 62px;
    letter-spacing: 5px;
    color: var(--white);
    line-height: 1;
  }
</style>
</head>
<body>
<main class="canvas">
  <section class="card card-front" aria-label="Card front">
    <svg class="shapes" width="660" height="377" viewBox="0 0 660 377">
      <rect class="edge-band" x="0" y="0" width="18" height="377" fill="var(--green)"/>
      <polygon class="chevron-stripe" points="478,0 496,0 436,188.5 496,377 478,377 418,188.5" fill="var(--white)"/>
      <polygon class="chevron-fill" points="506,0 660,0 660,377 506,377 446,188.5" fill="var(--green)"/>
    </svg>
    <div class="wordmark">
      <div class="wordmark-name">TRAVESCO</div>
      <div class="wordmark-sub">MINING</div>
    </div>
    <div class="contact">
      <div class="name">Dale Pemberton</div>
      <div class="title">Managing Director</div>
      <div><span class="label">Phone:</span> <span class="value">214-503-6192</span></div>
      <div><span class="label">Email:</span> <span class="value">Dale@Travesco-example.com</span></div>
      <div><span class="label">Address:</span> <span class="value">1185 Wexley #3 Dallas, TX 75211</span></div>
    </div>
  </section>

  <section class="card card-back" aria-label="Card back">
    <svg class="shapes" width="660" height="377" viewBox="0 0 660 377">
      <rect class="accent-band" x="110" y="0" width="60" height="377" fill="var(--green)"/>
    </svg>
    <div class="back-name">TRAVESCO</div>
  </section>
</main>
</body>
</html>
```